label bath salt on glass bottle

for our bath salts (Flavours Rose, Lavender, Lemongras, mountain herbs, Mint, Cashmere) we need a label in the size of 50mm height an 55mm wide.

Target Market(s)

Prestige stores

Font styles to use
Serif
Script

Colors

Designer to choose colors to be used in the design.

Requirements
Must have
• Name of the label:
• Headline: Badesalz (can be also written in two words) Bade Salz
• Describtion of the sel: Totes Meer (comes from Dead Sea)
• Name of the different fragrances:
• Rose
• Pfingstrose (Peony)
• Lemongras
• Alpenkräuter (mountain herbs)
• Minze (mint)
• Cashmere
• Lavendel (lavender)
Nice to have
• Made with love in Switzerland
• Logos:
• Use our LOGO in the attachment or just
• FENIVU
• Switzerland

```html
<!DOCTYPE html>
<html lang="de">
<head>
<meta charset="UTF-8">
<title>Badesalz Label</title>
<link rel="stylesheet" href="https://fonts.googleapis.com/css2?family=Kaushan+Script&family=Playfair+Display:wght@900&family=Lato:wght@300;400&family=Libre+Caslon+Text&display=swap">
<style>
  :root {
    --canvas-bg: #e4e4e4;
    --label-purple: #a27bb8;
    --label-white: #ffffff;
    --ink: #1a1a1a;
    --lavender-soft: #c9b3dc;
    --lavender-pale: #e6dbef;
    --text-grey: #2b2b2b;
    --variant-purple: #7d5a94;
  }
  * { margin: 0; padding: 0; box-sizing: border-box; }
  html, body {
    width: 1200px; height: 900px; overflow: hidden;
    background: var(--canvas-bg);
  }
  .canvas { position: relative; width: 1200px; height: 900px; }
  .label {
    position: absolute; left: 164px; top: 130px;
    width: 873px; height: 640px;
    background: var(--label-white);
    box-shadow: 0 18px 30px rgba(0,0,0,0.18);
    overflow: hidden;
  }
  .label-head {
    position: absolute; left: 0; top: 0; width: 100%; height: 279px;
    background: var(--label-purple);
  }
  .head-rule {
    position: absolute; left: 0; top: 279px; width: 100%; height: 9px;
    background: var(--ink);
  }
  .company-row {
    position: absolute; top: 52px; left: 131px; width: 625px; height: 50px;
    display: flex; align-items: center; gap: 18px;
  }
  .company-row .line { flex: 1; height: 2px; background: var(--ink); }
  .company-name {
    font-family: "Kaushan Script", cursive;
    font-size: 40px; color: var(--ink); line-height: 1;
  }
  .product-title {
    position: absolute; top: 100px; left: 0; width: 100%;
    text-align: center;
    font-family: "Playfair Display", serif; font-weight: 900;
    font-size: 96px; line-height: 1; color: var(--ink);
    letter-spacing: 1px;
  }
  .product-subtitle {
    position: absolute; top: 215px; left: 0; width: 100%;
    text-align: center;
    font-family: "Lato", sans-serif; font-weight: 300;
    font-size: 32px; letter-spacing: 22px; padding-left: 22px;
    color: var(--ink); line-height: 1;
  }
  .lavender-art {
    position: absolute; left: 236px; top: 302px;
    width: 400px; height: 128px;
    background: linear-gradient(160deg, var(--lavender-soft), var(--lavender-pale));
    border-radius: 40% 60% 50% 50% / 50% 40% 60% 50%;
    opacity: 0.85;
  }
  .note {
    position: absolute; top: 440px;
    font-family: "Lato", sans-serif; font-weight: 400;
    font-size: 36px; line-height: 48px; letter-spacing: 2px;
    color: var(--text-grey);
  }
  .note-left { left: 41px; text-align: left; }
  .note-right { right: 34px; text-align: right; letter-spacing: 1px; }
  .variant-list {
    position: absolute; top: 546px; left: 0; width: 100%;
    text-align: center;
    font-family: "Lato", sans-serif; font-weight: 400;
    font-size: 16px; letter-spacing: 2px; line-height: 1;
    color: var(--variant-purple);
  }
  .weight-row {
    position: absolute; top: 578px; left: 151px; width: 576px; height: 40px;
    display: flex; align-items: center; gap: 24px;
  }
  .weight-row .line { flex: 1; height: 2px; background: var(--text-grey); }
  .net-weight {
    font-family: "Libre Caslon Text", serif;
    font-size: 29px; color: var(--ink); line-height: 1;
  }
</style>
</head>
<body>
<div class="canvas">
  <div class="label">
    <div class="label-head">
      <div class="company-row">
        <span class="line"></span>
        <span class="company-name">YourCompany</span>
        <span class="line"></span>
      </div>
      <h1 class="product-title">BADESALZ</h1>
      <p class="product-subtitle">TOTES MEER</p>
    </div>
    <div class="head-rule"></div>
    <div class="lavender-art" role="img" aria-label="Line illustration of lavender sprigs"></div>
    <p class="note note-left">LOVELY<br>LAVENDEL</p>
    <p class="note note-right">CALMING<br>AROMATHERAPY</p>
    <p class="variant-list">ROSE · PFINGSTROSE · LEMONGRAS · ALPENKRÄUTER · MINZE · CASHMERE</p>
    <div class="weight-row">
      <span class="line"></span>
      <span class="net-weight">16 OZ (170GR)</span>
      <span class="line"></span>
    </div>
  </div>
</div>
</body>
</html>
```